Business card for a Exhibition booth fabrication company

Hi. My company would like to change our corporate name card. We are an events and Exhibition stand builder company. We would like our corporate name card to resonate what we do. I need someone to create something unique that relates to the industry that I am in. The graphic designer should be creative to incorporate the elements of my industry and try to blend in well in the design of the card. Our aim is to ensure that we are unique and our card can look different from our competitors.
Updates

The decision maker was very busy and didnt had time to make this decision

Target Market(s)

Marketing and events manager from all companies

Contact Information for Business Card

The business card should have the following details:
Name
Job Title
Email
Website

Colors

Designer to choose colors to be used in the design.

Requirements
Must have
• The card must be look something that is relevant to the service that I am providing. My website is: www.velmora-builds.com
• You can see my website to get more information on what service that I am doing
Nice to have
• On the back of my card, I would like to have a globe image with the incorporation of my company logo. This is to indicate that my services can be done in any part of the world.

```html
<!DOCTYPE html>
<html lang="en">
<head>
<meta charset="UTF-8">
<title>Velmora Builds – Business Card</title>
<link href="https://fonts.googleapis.com/css2?family=Jost:wght@400;500;600&display=swap" rel="stylesheet">
<style>
  :root {
    --stage: #3a3a3c;
    --brand-red: #d0202a;
    --brand-red-deep: #a8131b;
    --map-tone: #e0464c;
    --ink: #1c1c1c;
    --ink-soft: #4a4a4a;
    --paper: #ffffff;
  }
  * { margin: 0; padding: 0; box-sizing: border-box; }
  html, body { width: 1200px; height: 1000px; overflow: hidden; }
  body {
    background: var(--stage);
    font-family: "Jost", Arial, sans-serif;
    position: relative;
  }
  .card {
    position: absolute;
    left: 280px;
    width: 640px;
    height: 366px;
    border-radius: 26px;
    overflow: hidden;
    box-shadow: 0 14px 30px rgba(0,0,0,0.35);
  }
  /* Front */
  .card-front {
    top: 56px;
    background: linear-gradient(135deg, var(--brand-red) 0%, var(--brand-red-deep) 100%);
    color: var(--paper);
  }
  .world-map-area {
    position: absolute;
    inset: 20px 30px 60px 30px;
    border-radius: 120px;
    background: radial-gradient(ellipse at center, rgba(240,90,95,0.55) 0%, rgba(224,70,76,0.25) 55%, rgba(224,70,76,0) 80%);
  }
  .front-brand {
    position: absolute;
    top: 150px;
    left: 0; right: 0;
    text-align: center;
    display: flex;
    justify-content: center;
    align-items: center;
    gap: 14px;
  }
  .brand-dot {
    width: 22px; height: 22px; border-radius: 50%;
    background: var(--paper);
  }
  .brand-name {
    font-weight: 500;
    font-size: 30px;
    letter-spacing: 4px;
    text-transform: uppercase;
  }
  .front-web {
    position: absolute;
    bottom: 30px; left: 0; right: 0;
    text-align: center;
    font-size: 17px;
    font-weight: 500;
    letter-spacing: 0.5px;
  }
  /* Back */
  .card-back {
    top: 530px;
    background: var(--paper);
    color: var(--ink);
  }
  .name-marker {
    position: absolute;
    left: 0; top: 52px;
    width: 16px; height: 38px;
    background: var(--brand-red);
  }
  .holder { position: absolute; left: 36px; top: 48px; }
  .holder-name {
    color: var(--brand-red);
    font-size: 26px;
    font-weight: 500;
    line-height: 1.1;
  }
  .holder-title { font-size: 16px; color: var(--ink); }
  .contact-left { position: absolute; left: 36px; top: 138px; font-size: 19px; line-height: 1.3; }
  .contact-label { color: var(--brand-red); font-size: 17px; }
  .contact-row { display: flex; align-items: center; gap: 8px; }
  .icon { width: 18px; height: 18px; flex: none; }
  .back-brand {
    position: absolute;
    right: 40px; top: 70px;
    display: flex; align-items: center; gap: 12px;
  }
  .back-brand .brand-dot { background: var(--brand-red); }
  .back-brand .brand-name { color: var(--ink-soft); font-size: 26px; }
  .contact-right {
    position: absolute;
    right: 36px; bottom: 36px;
    font-size: 19px; line-height: 1.3;
    text-align: left;
  }
  .web-accent { color: var(--brand-red); }
</style>
</head>
<body>
  <section class="card card-front">
    <div class="world-map-area" role="img" aria-label="Faint world map spanning the red card"></div>
    <div class="front-brand">
      <span class="brand-dot"></span>
      <span class="brand-name">Velmora Builds</span>
    </div>
    <p class="front-web">www.velmora-builds.com</p>
  </section>

  <section class="card card-back">
    <span class="name-marker"></span>
    <div class="holder">
      <p class="holder-name">Adrian Kells</p>
      <p class="holder-title">President</p>
    </div>
    <div class="contact-left">
      <p class="contact-label">Singapore Contact:</p>
      <p>+65 81470226</p>
      <p class="contact-row">
        <svg class="icon" viewBox="0 0 18 18"><rect x="1" y="3" width="16" height="12" rx="2" fill="var(--brand-red)"/><path d="M2 4 L9 10 L16 4" stroke="#fff" stroke-width="1.5" fill="none"/></svg>
        info@velmora-builds.com
      </p>
    </div>
    <div class="back-brand">
      <span class="brand-dot"></span>
      <span class="brand-name">Velmora Builds</span>
    </div>
    <div class="contact-right">
      <p class="contact-label">Qatar Contact:</p>
      <p>+974 55208431</p>
      <p class="contact-row">
        <svg class="icon" viewBox="0 0 18 18"><circle cx="9" cy="9" r="7.5" fill="none" stroke="var(--brand-red)" stroke-width="1.6"/><ellipse cx="9" cy="9" rx="3.2" ry="7.5" fill="none" stroke="var(--brand-red)" stroke-width="1.3"/><line x1="1.5" y1="9" x2="16.5" y2="9" stroke="var(--brand-red)" stroke-width="1.3"/></svg>
        <span>www.<span class="web-accent">velmora-builds</span>.com</span>
      </p>
    </div>
  </section>
</body>
</html>
```